Business Card Design Project

Use our current logo. Clean design.

Industry/Entity Type

Business

Requirements
Must have
• Marisela DUBRANCQ
M. Law
Managing Partner

Alpenvorsa AG
Kornhalmweg 214
CH-3097 Liebefeld

M. +41 79 412 56 27
T. +41 31 928 44 10
F. +41 31 928 44 19

m.dubrancq@alpenvorsa-example.com
www.alpenvorsa-example.com

```html
<!DOCTYPE html>
<html lang="en">
<head>
<meta charset="utf-8">
<title>Alpenvorsa AG – Business Card</title>
<link rel="stylesheet" href="https://fonts.googleapis.com/css2?family=Cinzel:wght@400;600&display=swap">
<style>
  :root {
    --page: #ffffff;
    --brand-red: #b3121d;
    --ink: #111111;
    --back-black: #000000;
    --silver-light: #ffffff;
    --silver-mid: #e4e5e6;
    --silver-dark: #bcbdbf;
    --serif: "Cinzel", "Trajan Pro", serif;
  }
  * { margin: 0; padding: 0; box-sizing: border-box; }
  html, body {
    width: 1200px; height: 900px; overflow: hidden;
    background: var(--page);
    font-family: var(--serif);
    color: var(--ink);
  }
  .canvas { position: relative; width: 1200px; height: 900px; }

  .card { position: absolute; width: 498px; height: 300px; }
  .card--front { left: 189px; top: 129px; background: var(--brand-red); }
  .card--back  { left: 456px; top: 474px; background: var(--back-black); }

  .band {
    position: absolute; left: 0; top: 87px; width: 447px; height: 150px;
  }
  .card--front .band {
    background: radial-gradient(ellipse 150px 120px at 120px 75px,
      var(--silver-light) 0%, var(--silver-mid) 55%, var(--silver-dark) 100%);
  }
  .card--back .band {
    background:
      radial-gradient(ellipse 170px 130px at 150px 95px,
        var(--silver-light) 0%, var(--silver-mid) 55%, rgba(188,189,191,0) 100%),
      linear-gradient(90deg, var(--silver-dark) 0%, var(--silver-mid) 60%, var(--silver-dark) 88%, var(--silver-mid) 100%);
  }

  /* front */
  .brand-mark {
    position: absolute; left: 36px; top: 58px;
    display: flex; align-items: center; gap: 8px;
    font-weight: 600; font-size: 17px; letter-spacing: 1px; color: var(--ink);
  }
  .brand-mark__square { width: 12px; height: 12px; background: var(--ink); }
  .holder { position: absolute; left: 212px; top: 38px; text-align: center; }
  .holder__name {
    color: var(--brand-red); font-weight: 600; font-size: 18px; letter-spacing: 0.3px;
    white-space: nowrap;
  }
  .holder__roles {
    margin-top: 2px; font-size: 9.5px; font-weight: 600; letter-spacing: 0.3px;
    display: flex; justify-content: center; gap: 18px;
  }

  /* back */
  .address { position: absolute; left: 52px; top: 14px; line-height: 1; }
  .address__company { font-size: 20px; font-weight: 600; margin-bottom: 6px; }
  .address__line { font-size: 12.5px; font-weight: 600; margin-bottom: 7px; }
  .web { position: absolute; left: 52px; top: 109px; color: var(--brand-red); font-weight: 600; }
  .web__site { font-size: 12px; margin-bottom: 5px; }
  .web__mail { font-size: 10.5px; }
  .phones {
    position: absolute; right: 10px; top: 47px; text-align: right;
    font-size: 14px; line-height: 19px;
  }
</style>
</head>
<body>
<main class="canvas">
  <section class="card card--front" aria-label="Card front">
    <div class="band">
      <div class="brand-mark">
        <span class="brand-mark__square"></span>
        <span class="brand-mark__name">ALPENVORSA</span>
      </div>
      <div class="holder">
        <p class="holder__name">Marisela DUBRANCQ</p>
        <p class="holder__roles"><span>M. Law</span><span>Managing Partner</span></p>
      </div>
    </div>
  </section>

  <section class="card card--back" aria-label="Card back">
    <div class="band">
      <div class="address">
        <p class="address__company">Alpenvorsa AG</p>
        <p class="address__line">Kornhalmweg 214</p>
        <p class="address__line">CH-3097 Liebefeld</p>
      </div>
      <div class="web">
        <p class="web__site">www.alpenvorsa-example.com</p>
        <p class="web__mail">m.dubrancq@alpenvorsa-example.com</p>
      </div>
      <div class="phones">
        <p>M. +41 79 412 56 27</p>
        <p>T. +41 31 928 44 10</p>
        <p>F. +41 31 928 44 19</p>
      </div>
    </div>
  </section>
</main>
</body>
</html>
```